Sunny Ladle Kitchen April Competition

The website slider is 990 X 225 pixels to fit in with this website www.sunnyladlekitchen.com.au

We would love a fun, lively, food-oriented slider created for Sunny Ladle Kitchen website. Sunny Ladle Kitchen is a central place where people who love food, cooking for their family and friends, and sharing recipes can hang out. We'd like the sliders to be simple, bright and to entice people to click on the link.

The banner ad needs to feature the Coastal Readers' Monthly cookbooks, and to use a colour scheme that also works with the existing website.

A slider in March was used to promote a similar competition which I will upload as inspiration, along with the image of the cook books to use.

Main text: Add your best mid-week meal recipes to win one of 8 cookbook sets!
Smaller text: The 8 best recipes as chosen by Sunny Ladle Kitchen editors will win.

```html
<!DOCTYPE html>
<html lang="en">
<head>
<meta charset="utf-8">
<title>Sunny Ladle Kitchen</title>
<link rel="stylesheet" href="https://fonts.googleapis.com/css2?family=Arimo:wght@400;700&family=Questrial&family=Caveat:wght@500&family=Patrick+Hand+SC&display=swap">
<style>
:root{
  --paper:#efe6da;
  --white:#ffffff;
  --cream:#fdfaf1;
  --card:#f8f2ea;
  --orange:#d9532a;
  --orange-dark:#c44620;
  --link:#d9532a;
  --ink:#333333;
  --brown:#4a3a33;
  --star:#c9575c;
  --sand:#f2cf97;
  --line:#e4dbd0;
}
*{box-sizing:border-box;margin:0;padding:0}
html,body{width:1200px;height:822px;overflow:hidden}
body{background:var(--paper);font-family:"Arimo",Arial,sans-serif;color:var(--ink);position:relative}
.abs{position:absolute}

.account{left:923px;top:0;width:106px;height:25px;background:var(--white);border-radius:0 0 4px 4px;font-size:12px;color:var(--link);display:flex;gap:10px;justify-content:center;align-items:center}
.brand{left:172px;top:36px;display:flex;align-items:center;gap:8px}
.brand-dot{width:14px;height:14px;border-radius:50%;background:var(--orange);flex:none}
.brand-name{font-family:"Arimo",Arial,sans-serif;font-weight:700;font-size:19px;line-height:22px;color:var(--brown)}
.tagline{left:458px;top:30px;font-family:"Caveat",cursive;font-size:28px;color:var(--brown)}
.tagline-arrow{left:766px;top:34px}

.nav-tabs{left:326px;top:87px;width:266px;height:36px;background:var(--white);display:flex;align-items:center;padding-left:20px;gap:18px;font-size:11px;font-weight:700;color:var(--ink)}
.nav-tabs span{display:flex;align-items:center;gap:4px}
.nav-links{left:592px;top:87px;width:437px;height:36px;background:var(--orange);border-radius:0 4px 0 0;display:flex;align-items:center;padding-left:28px;font-size:11px;font-weight:700;color:var(--white)}
.nav-links span+span::before{content:"•";margin:0 8px}

.hero{left:165px;top:123px;width:864px;height:199px;background:var(--cream)}
.hero-copy{left:0;top:14px;width:410px;text-align:center;font-family:"Questrial",sans-serif;color:var(--brown)}
.hero-title{font-family:"Patrick Hand SC",cursive;font-size:52px;line-height:46px;letter-spacing:1.5px;white-space:nowrap}
.hero-main{font-size:21px;line-height:25px}
.hero-small{font-size:14px;line-height:19px;margin-top:4px}
.hero-btn{display:inline-block;margin-top:8px;background:var(--orange);color:var(--white);font-size:15px;padding:4px 8px;border:1px solid var(--orange-dark);letter-spacing:.5px}
.hero-books{left:420px;top:40px;width:175px;height:120px;background:linear-gradient(100deg,#39a6c4,#d8344a 45%,#3a9fc0);border-radius:4px}
.hero-photo{left:585px;top:0;width:279px;height:199px;background:linear-gradient(180deg,#f1ece4,#e6ddd2 60%,#b9b1a6)}

.content{left:165px;top:322px;width:864px;height:500px;background:var(--white)}
.section-title{font-size:18px;color:var(--ink);display:flex;align-items:center;gap:10px;font-weight:400}

.card{top:61px;width:174px;height:237px;background:var(--card);border-bottom:4px solid var(--sand)}
.card-img{height:118px}
.card-name{font-size:12px;margin:13px 0 0 9px}
.card-by{font-size:10.5px;color:var(--link);margin:8px 0 0 9px}
.card-foot{position:absolute;left:9px;right:9px;bottom:9px;display:flex;justify-content:space-between;align-items:center;font-size:10px}
.card-foot .count{display:flex;align-items:center;gap:4px}

.browse{left:9px;top:325px;width:558px;height:126px;box-shadow:0 1px 4px rgba(0,0,0,.15)}
.browse-bar{height:36px;background:var(--orange);border-top:3px solid #f0a27f;display:flex;align-items:center;color:var(--white);font-size:12px}
.browse-bar span{width:182px;flex:none;display:flex;align-items:center;gap:6px;padding-left:6px}
.browse-links{display:flex;padding:12px 0 0 26px;font-size:12px;color:var(--link)}
.browse-links ul{list-style:none;display:grid;grid-template-columns:73px 73px;row-gap:9px;width:182px;flex:none}

.search{left:593px;top:13px;width:260px;height:34px;background:#fbf2ea;border:1px solid var(--line);border-radius:3px;font-size:12px;font-style:italic;color:var(--ink);padding:10px}
.search-icon{position:absolute;right:12px;top:7px}
.search-type{left:736px;top:53px;font-size:11px;display:flex;gap:6px;align-items:center}
.radio{width:9px;height:9px;border-radius:50%;border:1px solid #999;display:inline-block;background:#eee}
.radio.on{background:radial-gradient(#3a70c0 35%,#eee 45%)}

.rated{left:593px;width:260px;height:80px}
.rated-img{width:117px;height:78px}
.rated-num{position:absolute;left:-11px;top:24px;width:30px;height:30px;border-radius:50%;background:var(--white);font-size:11px;color:var(--link);display:flex;align-items:center;justify-content:center}
.rated-text{position:absolute;left:126px;top:0;width:136px;font-size:11.5px;line-height:17px}
.rated-text .by{color:var(--link)}
.rated-stars{position:absolute;left:126px;top:67px}
</style>
</head>
<body>
<svg width="0" height="0" style="position:absolute">
  <defs>
    <symbol id="star" viewBox="0 0 20 20"><polygon points="10,1 12.6,7 19,7.4 14,11.6 15.6,18 10,14.5 4.4,18 6,11.6 1,7.4 7.4,7" fill="var(--star)"/></symbol>
    <symbol id="bowl" viewBox="0 0 20 16"><path d="M1 6h18a9 8 0 0 1-18 0z" fill="var(--orange)"/><line x1="12" y1="6" x2="18" y2="0" stroke="var(--orange)" stroke-width="2"/></symbol>
  </defs>
</svg>

<div class="abs account"><span>Register</span><span>Login</span></div>
<div class="abs brand"><span class="brand-dot"></span><span class="brand-name">Sunny Ladle<br>Kitchen</span></div>
<div class="abs tagline">Join the community now!</div>
<svg class="abs tagline-arrow" width="42" height="24" viewBox="0 0 42 24"><path d="M2 20 Q20 4 38 6" fill="none" stroke="var(--orange)" stroke-width="2"/><path d="M31 2 L38 6 L32 11" fill="none" stroke="var(--orange)" stroke-width="2"/></svg>

<nav class="abs nav-tabs">
  <span><svg width="18" height="14"><use href="#bowl"/></svg>Recipes</span>
  <span><svg width="16" height="14" viewBox="0 0 16 14"><path d="M3 8a4 4 0 0 1 2-7 4 4 0 0 1 6 0 4 4 0 0 1 2 7v5H3z" fill="var(--orange)"/></svg>Chefs</span>
  <span><svg width="16" height="14" viewBox="0 0 16 14"><circle cx="4" cy="4" r="2" fill="var(--orange)"/><circle cx="8" cy="2.5" r="2" fill="var(--orange)"/><circle cx="12" cy="4" r="2" fill="var(--orange)"/><ellipse cx="8" cy="10" rx="4" ry="3.5" fill="var(--orange)"/></svg>Mentors</span>
</nav>
<nav class="abs nav-links"><span>Upload your recipe</span><span>Prizes</span><span>About</span><span>FAQs</span><span>Contact</span><span>Blog</span></nav>

<section class="abs hero">
  <div class="abs hero-copy">
    <div class="hero-title">ADD YOUR BEST</div>
    <div class="hero-main">mid-week meal recipes<br>to win one of 8 cookbook sets!</div>
    <div class="hero-small">The 8 best recipes as chosen<br>by Sunny Ladle Kitchen editors will win.</div>
    <div class="hero-btn">FIND OUT MORE HERE</div>
  </div>
  <div class="abs hero-books" role="img" aria-label="Three Coastal Readers' Monthly cookbooks fanned out"></div>
  <div class="abs hero-photo" role="img" aria-label="Home cook chopping fresh vegetables in a bright kitchen"></div>
</section>

<main class="abs content">
  <h2 class="abs section-title" style="left:10px;top:22px"><svg width="18" height="14"><use href="#bowl"/></svg>Featured Recipes</h2>

  <article class="abs card" style="left:9px">
    <div class="card-img" role="img" aria-label="Open cacciatore lasagne on a white plate" style="background:linear-gradient(#d8cfc4,#b9683d 60%,#e9e2d8)"></div>
    <div class="card-name">Open Cacciatore Lasagne</div>
    <div class="card-by">By Corinne Delaney</div>
    <div class="card-foot"><svg width="70" height="14"><use href="#star" width="14" height="14"/><use href="#star" x="14" width="14" height="14"/><use href="#star" x="28" width="14" height="14"/><use href="#star" x="42" width="14" height="14"/><use href="#star" x="56" width="14" height="14" opacity=".35"/></svg><span class="count"><svg width="18" height="14"><use href="#bowl"/></svg>10</span></div>
  </article>
  <article class="abs card" style="left:201px">
    <div class="card-img" role="img" aria-label="Spaghetti bolognaise topped with cheese" style="background:linear-gradient(#6e3a32,#8a4a3a 50%,#e6c98f)"></div>
    <div class="card-name">Spaghetti Bolognaise</div>
    <div class="card-by">By Lydia Summers</div>
    <div class="card-foot"><svg width="70" height="14"><use href="#star" width="14" height="14"/><use href="#star" x="14" width="14" height="14"/><use href="#star" x="28" width="14" height="14"/><use href="#star" x="42" width="14" height="14"/><use href="#star" x="56" width="14" height="14"/></svg><span class="count"><svg width="18" height="14"><use href="#bowl"/></svg>4</span></div>
  </article>
  <article class="abs card" style="left:393px">
    <div class="card-img" role="img" aria-label="Bowl of clear vegetable stock" style="background:linear-gradient(#cfc6b6,#7a7a2e 55%,#c9c0ac)"></div>
    <div class="card-name">Clean Eating Vegetable Stock</div>
    <div class="card-by">By Janet Holloway</div>
    <div class="card-foot"><svg width="70" height="14"><use href="#star" width="14" height="14"/><use href="#star" x="14" width="14" height="14"/><use href="#star" x="28" width="14" height="14"/><use href="#star" x="42" width="14" height="14"/><use href="#star" x="56" width="14" height="14"/></svg><span class="count"><svg width="18" height="14"><use href="#bowl"/></svg>3</span></div>
  </article>

  <section class="abs browse">
    <div class="browse-bar"><span>● Browse by Meal</span><span>● Browse by Occasion</span><span>● Browse by Diet</span></div>
    <div class="browse-links">
      <ul><li>Dinner</li><li>Lunch</li><li>Dessert</li><li>Baking</li><li>Snacks</li><li>Entree</li></ul>
      <ul><li>Summer</li><li>Parties</li><li>Winter</li><li>Kids</li><li>Barbeques</li><li>Christmas</li></ul>
      <ul><li>Healthy</li><li>Vegetarian</li><li>Dairy Free</li><li>Gluten-Free</li><li>Vegan</li><li>Weightloss</li></ul>
    </div>
  </section>

  <h2 class="abs section-title" style="left:10px;top:471px"><svg width="18" height="14"><use href="#bowl"/></svg>Popular Recipes</h2>

  <div class="abs search">search<svg class="search-icon" width="20" height="20" viewBox="0 0 20 20"><circle cx="8" cy="8" r="6" fill="none" stroke="#f2b84a" stroke-width="2.5"/><line x1="12.5" y1="12.5" x2="18" y2="18" stroke="#f2b84a" stroke-width="3"/></svg></div>
  <div class="abs search-type"><span>Recipes</span><span class="radio on"></span><span style="margin-left:12px">Chefs</span><span class="radio"></span></div>

  <h2 class="abs section-title" style="left:595px;top:84px"><svg width="18" height="14"><use href="#bowl"/></svg>Highest Rated Recipes</h2>

  <div class="abs rated" style="top:122px">
    <div class="rated-img" role="img" aria-label="White chocolate parfait with lemon curd" style="background:linear-gradient(#8a6a3a,#f2dfa0 50%,#5a3b22)"></div>
    <div class="rated-num">1</div>
    <div class="rated-text">White Chocolate Parfait W/ Lemon Curd and Short ..<br><span class="by">By Simon Tarrant</span></div>
    <svg class="rated-stars" width="70" height="14"><use href="#star" width="14" height="14"/><use href="#star" x="14" width="14" height="14"/><use href="#star" x="28" width="14" height="14"/><use href="#star" x="42" width="14" height="14"/><use href="#star" x="56" width="14" height="14"/></svg>
  </div>
  <div class="abs rated" style="top:218px">
    <div class="rated-img" role="img" aria-label="Tray of hot cross buns" style="background:linear-gradient(#3a2a22,#b98a5a 50%,#7a4a2a)"></div>
    <div class="rated-num">2</div>
    <div class="rated-text">Hot Cross Buns<br><span class="by">By Mira Gallo</span></div>
    <svg class="rated-stars" width="70" height="14"><use href="#star" width="14" height="14"/><use href="#star" x="14" width="14" height="14"/><use href="#star" x="28" width="14" height="14"/><use href="#star" x="42" width="14" height="14"/><use href="#star" x="56" width="14" height="14"/></svg>
  </div>
  <div class="abs rated" style="top:314px">
    <div class="rated-img" role="img" aria-label="Roast pork belly with potatoes and apple puree" style="background:linear-gradient(#1e1a18,#e8dccb 55%,#2a2420)"></div>
    <div class="rated-num">3</div>
    <div class="rated-text">Roast Pork Belly with Potatoes and Apple Puree<br><span class="by">By Sophie Lennox</span></div>
    <svg class="rated-stars" width="70" height="14"><use href="#star" width="14" height="14"/><use href="#star" x="14" width="14" height="14"/><use href="#star" x="28" width="14" height="14"/><use href="#star" x="42" width="14" height="14"/><use href="#star" x="56" width="14" height="14"/></svg>
  </div>
  <div class="abs rated" style="top:410px">
    <div class="rated-img" role="img" aria-label="Spicy lemongrass chicken with coconut juice" style="background:linear-gradient(#6f8fb5,#4f7a3a 55%,#c26a3a)"></div>
    <div class="rated-num">4</div>
    <div class="rated-text">Spicy Lemongrass Chicken with Coconut Juice<br><span class="by">By Sophie Lennox</span></div>
    <svg class="rated-stars" width="70" height="14"><use href="#star" width="14" height="14"/><use href="#star" x="14" width="14" height="14"/><use href="#star" x="28" width="14" height="14"/><use href="#star" x="42" width="14" height="14"/><use href="#star" x="56" width="14" height="14"/></svg>
  </div>
</main>
</body>
</html>
```